Website Redesign for Technology Focused Investment Bank

We need a website redesign for a technology and digital media focused investment banking firm. Think modern and forward thinking yet stable and smart. We provide mergers and acquisitions advisory services to our clients. Our target market are CEO's and CFO's (senior executives) that run and operate technology firms.

Kestrel Bay Advisors - www.kestrelbayadvisors.example

We are headquartered in Los Angeles, CA. Please do NOT use the Brindle Arch for anything.

We have the content and can update the photos as well.

We are looking for a "template" website we can update and edit with ease.

A competitive firm's website is: www.dunmoregrey.example Not sure I like it but I want it to look way better then this one.

Looking for a more modern version. Not too stuffy and conservative, please. Elegant, smart, updated and progressive/modern.
Updates

Color preferences:  Blue's including matching logo color. Grey's. You can add other colors if it flows well and looks clean and nice.

Menu:  Drop Down

Open to platform...please use one that most people can use, is reasonably priced if I need to buy it, and easy to update monthly and sometimes weekly.

Please use this website as a good example of what we are looking for (or similar version of it): www.plorvex.example

Thanks!
Tobias R.

We are reviewing all submissions and will select one this week. Thank you everyone for your outstanding and creative designs you have sent us. We really appreciate it.

Thanks for everyone's hard work and creative input into our website design. We really appreciate it!

Target Market(s)

CEO's and CFO's, Entrepreneurs and Board Members of Technology Companies.

Industry/Entity Type

Investment

Font styles to use
Sans Serif

Colors
33a6d7
0492cd
0555a3
3176b5
85abd2
333333
5c5c5c
757575

Requirements
Must have
• Links to social media including Twitter, LinkedIn, Google+, Facebook, etc.

Must try to match logo color
Should not have
• No conservative, old looking colors or background. For example, no green marble look.

```html
<!DOCTYPE html>
<html lang="en">
<head>
<meta charset="utf-8">
<title>Kestrel Bay Advisors</title>
<link rel="stylesheet" href="https://fonts.googleapis.com/css2?family=Arimo:wght@400;700&family=Fira+Sans:ital,wght@1,500&display=swap">
<style>
:root{
  --blue-dark:#0555a3;
  --blue:#3176b5;
  --blue-bright:#0492cd;
  --blue-sky:#33a6d7;
  --blue-soft:#85abd2;
  --ink:#333333;
  --ink-mid:#5c5c5c;
  --ink-light:#757575;
  --page:#eeeeee;
  --white:#ffffff;
  --rule:#d4d4d4;
}
*{box-sizing:border-box;margin:0;padding:0}
html,body{width:1098px;height:1200px;overflow:hidden}
body{position:relative;background:var(--page);font-family:"Arimo",Arial,sans-serif;color:var(--ink);font-size:11px}
a{color:inherit;text-decoration:none}
.abs{position:absolute}

/* header */
.header{left:0;top:0;width:1098px;height:140px;background:var(--white)}
.brand{left:157px;top:16px;display:flex;align-items:center;gap:24px}
.brand-mark{width:88px;height:88px;border-radius:50%;background:radial-gradient(circle at 40% 35%,var(--blue-soft),var(--blue-dark) 75%)}
.brand-name{font-size:26px;color:var(--blue-dark);font-weight:400}
.lang{left:876px;top:16px;width:66px;height:19px;background:var(--blue-bright);color:var(--white);font-weight:700;font-size:11px;line-height:19px;padding-left:6px;border-radius:2px}
.lang::after{content:"";position:absolute;right:7px;top:8px;border:4px solid transparent;border-top-color:var(--white)}
.social{display:flex;gap:5px}
.social span{width:17px;height:17px;border-radius:2px}
.s1{background:#3b5998}.s2{background:var(--blue-sky)}.s3{background:var(--blue-dark)}.s4{background:#f5871f}
.head-social{left:858px;top:43px}
.phone{left:792px;top:68px;display:flex;align-items:center;gap:8px;font-weight:700;font-size:14px;color:var(--ink)}

/* nav */
.band{left:0;top:140px;width:1098px;height:368px;background:linear-gradient(var(--blue-dark),var(--blue))}
.nav{left:157px;top:118px;width:785px;height:40px;background:#f4f4f4;display:flex;align-items:center;justify-content:space-between;padding:0 10px;border-radius:2px}
.nav a{font-size:13px;color:var(--ink-mid)}
.nav a.active{color:var(--blue-dark)}

/* hero */
.hero{left:157px;top:177px;width:785px;height:313px;background:var(--white);border-radius:3px}
.hero-photo{left:7px;top:7px;width:534px;height:297px;background:linear-gradient(#1e6fcf,#5fb2ea 60%,#b9cde8)}
.dots{left:56px;top:270px;display:flex;gap:5px;align-items:center;color:var(--white);font-size:14px}
.dots i{width:7px;height:7px;border-radius:50%;background:var(--white);display:block}
.dots i.on{background:none;border:1.5px solid var(--white)}
.hero-divide{left:548px;top:0;width:12px;height:313px;background:linear-gradient(90deg,#e4e4e4,var(--white))}
.hero-title{left:568px;top:36px;width:215px;font-family:"Fira Sans",sans-serif;font-style:italic;font-weight:500;font-size:22.5px;line-height:33px;color:var(--blue-bright)}
.btn{left:567px;top:248px;height:24px;padding:0 9px;background:var(--blue-dark);color:var(--white);font-weight:700;font-size:11px;line-height:24px;border-radius:3px}

/* sections */
.sec-head{display:flex;align-items:center;gap:10px;color:var(--blue);font-weight:700;border-bottom:1px solid var(--rule)}
.orb{width:34px;height:34px;border-radius:50%;background:radial-gradient(circle at 40% 35%,var(--blue-soft),var(--blue-dark) 75%);flex:none}
.why-head{left:157px;top:524px;width:509px;height:40px;font-size:22px}
.why-text{left:157px;top:572px;width:308px;font-size:10.5px;line-height:14.6px;color:var(--ink-mid);text-align:justify;letter-spacing:.2px}
.why-text p{margin-bottom:12px}
.why-more{left:380px;top:836px;font-weight:700;font-size:11px;color:var(--blue)}
.portrait{left:486px;top:574px;width:180px;height:276px;background:#000;padding:4px}
.portrait div{width:100%;height:100%;border:1px solid #bbb;background:linear-gradient(#111,#2a2a2a)}

.panel{background:var(--white);border:1px solid #dcdcdc;border-radius:2px}
.blog{left:707px;top:530px;width:235px;height:319px;padding:12px 14px}
.blog-head{display:flex;align-items:center;gap:8px;font-size:16px;font-weight:700;color:var(--blue);padding-bottom:10px;border-bottom:2px solid var(--rule)}
.rss{width:20px;height:20px;background:#f5871f;border-radius:2px}
.arrows{margin-left:auto;color:var(--ink-mid);font-size:20px;font-weight:400;letter-spacing:3px}
.post{padding:13px 0 11px;border-bottom:1px dotted #bbb}
.post:last-child{border:0}
.post b{display:block;font-size:10.5px;margin-bottom:5px}
.post a{color:var(--blue-bright);font-size:10px;line-height:13.5px;display:block}

.svc-head{left:157px;top:880px;width:509px;height:38px;font-size:18px}
.svc-list{left:157px;top:928px;width:509px;height:120px;display:grid;grid-template-columns:274px 235px;grid-auto-flow:column;grid-template-rows:repeat(4,26px);list-style:none;font-weight:700;font-size:11px;border-bottom:1px solid var(--rule)}
.svc-list li::before{content:"• ";color:var(--blue-dark)}

.feed-head{left:707px;top:880px;width:235px;height:38px;font-size:18px;color:var(--blue);font-weight:700;display:flex;align-items:center;gap:10px}
.feed{left:706px;top:918px;width:236px;height:132px;padding:6px 10px}
.post-item{display:flex;gap:10px;padding:9px 0 8px 8px;font-size:10px;line-height:13.5px}
.post-item+.post-item{border-top:1px solid var(--rule)}
.post-item p{color:var(--ink);width:170px}
.fdot{width:14px;height:14px;border-radius:50%;background:var(--blue-sky);flex:none;margin-top:2px}
.post-item a{color:var(--blue-dark)}
.post-item small{display:block;color:var(--ink-light);font-size:10px;margin-top:3px}

/* footer */
.foot-rule{left:157px;top:1075px;width:785px;height:4px;border-top:1px solid #999;border-bottom:1px solid #999;background:repeating-linear-gradient(90deg,#aaa 0 1px,transparent 1px 3px)}
.foot-nav{left:0;top:1093px;width:1098px;text-align:center;font-size:10.5px;color:var(--ink)}
.foot-nav span{margin:0 5px}
.foot-contact{left:0;top:1116px;width:1098px;display:flex;justify-content:center;align-items:center;gap:14px;font-size:10.5px}
.foot-social{left:507px;top:1145px}
.copy{left:0;top:1173px;width:1098px;text-align:center;font-size:10px}
</style>
</head>
<body>
<header class="abs header">
  <a class="abs brand" href="#"><span class="brand-mark"></span><span class="brand-name">Kestrel Bay Advisors</span></a>
  <div class="abs lang">English</div>
  <div class="abs social head-social"><span class="s1"></span><span class="s2"></span><span class="s3"></span><span class="s4"></span></div>
  <div class="abs phone">
    <svg width="24" height="24" viewBox="0 0 24 24"><path d="M6 2l4 4-2 3c1 3 4 6 7 7l3-2 4 4-3 4C10 21 3 14 2 5z" fill="#0555a3"/></svg>
    +1 (310) 555-0147
  </div>
</header>

<div class="abs band"></div>
<nav class="abs nav">
  <a class="active" href="#">About Us</a><a href="#">Services</a><a href="#">Transactions</a><a href="#">Research</a><a href="#">Private Equity</a><a href="#">Recommendations</a><a href="#">About the Founder</a><a href="#">Careers</a><a href="#">News+Blog</a>
</nav>

<section class="abs hero">
  <div class="abs hero-photo" role="img" aria-label="Hand moving a chess piece against a blue sky">
    <div class="abs dots">‹ <i class="on"></i><i></i><i></i><i></i><i></i><i></i> ›</div>
  </div>
  <div class="abs hero-divide"></div>
  <h1 class="abs hero-title">Investment Banking<br>and M&amp;A Advisory<br>for Software,<br>IT Services and<br>Digital<br>Media Companies</h1>
  <a class="abs btn" href="#">READ MORE</a>
</section>

<h2 class="abs sec-head why-head"><span class="orb"></span>Why Us?</h2>
<div class="abs why-text">
  <p>We are an independent investment bank and M&amp;A advisory firm focused exclusively on the global Technology and Digital Media sectors. Specifically, we execute mergers and acquisitions for the Software, IT Services, Internet and Digital Media industry sectors.</p>
  <p>Our professionals have completed over $20 billion in transactions to date and have experience in investment banking, private equity and capital markets from leading firms. We are experts in complex M&amp;A transactions of most shapes and sizes and have deep industry expertise.</p>
  <p>We advise companies, entrepreneurs, majority shareholders and leading institutions on complex strategic and financial transactions including mergers, acquisitions, divestitures, asset sales, spin-offs and related corporate finance issues that create and increase shareholder value.</p>
</div>
<a class="abs why-more" href="#">READ MORE [+]</a>
<div class="abs portrait"><div role="img" aria-label="Portrait of the founder in a dark suit"></div></div>

<aside class="abs panel blog">
  <div class="blog-head"><span class="rss"></span>FROM OUR BLOG<span class="arrows">‹›</span></div>
  <div class="post"><b>06/03/2014</b><a href="#">Lorem ipsum dolor sit amet, consectetuer nibh euismod tincidunt ut laoreet</a></div>
  <div class="post"><b>06/03/2014</b><a href="#">Lorem ipsum dolor sit amet, consectetuer nibh euismod tincidunt ut laoreet</a></div>
  <div class="post"><b>06/03/2014</b><a href="#">Lorem ipsum dolor sit amet, consectetuer nibh euismod tincidunt ut laoreet</a></div>
  <div class="post"><b>06/03/2014</b><a href="#">Lorem ipsum dolor sit amet, consectetuer nibh euismod tincidunt ut laoreet</a></div>
</aside>

<h2 class="abs sec-head svc-head"><span class="orb"></span>Services We Provide</h2>
<ul class="abs svc-list">
  <li>Buy-Side Mergers and Acquisitions</li>
  <li>Sell-Side Mergers and Acquisitions</li>
  <li>Recapitalizations and Restructuring's</li>
  <li>Equity and Debt Buyout Financing (Advisory)</li>
  <li>Spin-Offs and Asset Sales</li>
  <li>Strategic and Corporate Finance Advisory</li>
  <li>Fairness Opinions and Valuations</li>
</ul>

<h2 class="abs feed-head"><span class="orb"></span>Social Feeds<span class="arrows">‹›</span></h2>
<aside class="abs panel feed">
  <div class="post-item"><span class="fdot"></span><p><a href="#">Lorem ipsum</a> dolor sit amet,<br>consectetur adipiscing <a href="#">elit Praesent</a><small>3 days 6 hours ago</small></p></div>
  <div class="post-item"><span class="fdot"></span><p><a href="#">Lorem ipsum</a> dolor sit amet,<br>consectetur adipiscing <a href="#">elit Praesent</a><small>3 days 6 hours ago</small></p></div>
</aside>

<footer>
  <div class="abs foot-rule"></div>
  <nav class="abs foot-nav">Home<span>|</span>About Us<span>|</span>Services<span>|</span>Transactions<span>|</span>Research<span>|</span>Private Equity<span>|</span>Recommendations<span>|</span>About the Founder<span>|</span>Careers<span>|</span>News+Blog<span>|</span>Contact Us</nav>
  <div class="abs foot-contact">
    <svg width="20" height="20" viewBox="0 0 20 20"><circle cx="10" cy="10" r="9" fill="none" stroke="#0555a3" stroke-width="1.5"/><path d="M7 5l2 2-1 2c.5 1.5 1.5 2.5 3 3l1-1 2 2-1.5 1.5C8.5 14 6 11.5 5.5 6.5z" fill="#0555a3"/></svg>
    <span>mergers@kestrelbayadvisors.example</span>
    <svg width="22" height="15" viewBox="0 0 22 15"><rect width="22" height="15" fill="#0555a3"/><path d="M0 0l11 8 11-8M0 15l8-7M22 15l-8-7" fill="none" stroke="#fff" stroke-width="1.2"/></svg>
    <span>+1 (310) 555-0147</span>
  </div>
  <div class="abs social foot-social"><span class="s1"></span><span class="s2"></span><span class="s3"></span><span class="s4"></span></div>
  <p class="abs copy">© 2014 Kestrel Bay Advisors. All Rights Reserved</p>
</footer>
</body>
</html>
```